Exciting Personal Development Book Cover: FIND ZEN NOW!

Design a Book Cover for my personal development book.
Title: Find Zen Now!
Author: Marcus Telly
Tagline: A real-life solution to get unstuck and break free

My picture must make up the front cover as I need to build my brand and people should recognise me on book shelves. Bold and catchy. How you do it is up to you. There must be space for a short testimonial from a famous person who is currently reading my book. I uploaded a sample of what I made in Photoshop but I don't have design skills.

I've added a PDF of my book so you can read the chapter index and introduction to get a sense of the content.

Target Market(s)

Personal Development Self-Help Market

Industry/Entity Type

Personal Development

Font styles to use
Serif
Sans Serif

Requirements
Must have
• My picture as hero image on cover.
Nice to have
• Must have Title, Tagline and my author name. If possible ZEN stands for 'Zeal, Energy & Nerve' If there is a way to fit this somewhere great. If it's too much then it can go somewhere on the back.

```html
<!DOCTYPE html>
<html lang="en">
<head>
<meta charset="utf-8">
<title>Find Zen Now! – Book Cover</title>
<link rel="stylesheet" href="https://fonts.googleapis.com/css2?family=Anton&family=Montserrat:ital,wght@0,800;1,800&display=swap">
<style>
  :root {
    --backdrop: #d9d9d9;
    --cover-top: #5d646c;
    --cover-bottom: #7e858c;
    --spine: #4f565e;
    --accent: #00aeef;
    --ink-light: #ffffff;
    --photo-pale: #d4d6d9;
    --photo-warm: #a79a92;
  }
  html, body {
    margin: 0;
    padding: 0;
    width: 1200px;
    height: 801px;
    overflow: hidden;
    background: var(--backdrop);
  }
  .book-cover {
    position: absolute;
    left: 332px;
    top: 20px;
    width: 536px;
    height: 761px;
    background: linear-gradient(180deg, var(--cover-top) 0%, var(--cover-bottom) 100%);
    overflow: hidden;
    box-shadow: 0 6px 18px rgba(0,0,0,0.18);
  }
  .cover-spine {
    position: absolute;
    left: 0;
    top: 0;
    width: 37px;
    height: 100%;
    background: var(--spine);
  }
  .author-photo {
    position: absolute;
    left: 80px;
    top: 250px;
    width: 420px;
    height: 470px;
    background:
      radial-gradient(ellipse 45% 20% at 50% 28%, var(--photo-warm) 0%, transparent 100%),
      radial-gradient(ellipse 55% 50% at 50% 62%, var(--photo-pale) 0%, rgba(212,214,217,0.55) 55%, transparent 100%);
  }
  .title {
    position: absolute;
    left: 37px;
    right: 0;
    top: 34px;
    margin: 0;
    display: flex;
    justify-content: center;
    align-items: stretch;
    gap: 6px;
    font-family: "Anton", "Impact", sans-serif;
    font-weight: 400;
    line-height: 0.86;
    text-transform: uppercase;
  }
  .title-word {
    display: block;
    color: var(--ink-light);
    font-size: 66px;
  }
  .title-word--lead { align-self: flex-start; margin-top: 14px; }
  .title-word--tail { align-self: flex-end; }
  .title-word--key {
    color: var(--accent);
    font-size: 168px;
    letter-spacing: -3px;
  }
  .tagline {
    position: absolute;
    left: 37px;
    right: 0;
    top: 206px;
    margin: 0;
    text-align: center;
    font-family: "Montserrat", "Arial", sans-serif;
    font-weight: 800;
    font-size: 10.5px;
    line-height: 1.2;
    color: var(--ink-light);
    letter-spacing: 0.2px;
  }
  .tagline .initial { color: var(--accent); }
  .author-name {
    position: absolute;
    left: 37px;
    right: 0;
    top: 660px;
    margin: 0;
    text-align: center;
    font-family: "Anton", "Impact", sans-serif;
    font-weight: 400;
    font-size: 62px;
    line-height: 1;
    color: var(--accent);
    letter-spacing: 1px;
    text-transform: uppercase;
  }
  .testimonial {
    position: absolute;
    left: 37px;
    right: 0;
    top: 734px;
    margin: 0;
    text-align: center;
    font-family: "Montserrat", "Arial", sans-serif;
    font-weight: 800;
    font-size: 11.5px;
    color: var(--ink-light);
  }
  .testimonial cite { font-style: italic; }
</style>
</head>
<body>
  <main class="book-cover">
    <div class="cover-spine"></div>

    <div class="author-photo" role="img" aria-label="Portrait photograph of the author Marcus Telly in a white shirt"></div>

    <h1 class="title">
      <span class="title-word title-word--lead">Find</span>
      <span class="title-word title-word--key">Zen</span>
      <span class="title-word title-word--tail">Now!</span>
    </h1>

    <p class="tagline">
      STACKING <span class="initial">Z</span>EAL, <span class="initial">E</span>NERGY AND <span class="initial">N</span>ERVE TO OVERCOME PAIN<br>
      AND THE OBSTACLES OF LIFE
    </p>

    <p class="author-name">Marcus Telly</p>

    <p class="testimonial">‘Occus, quiaess itaspiti doluptas alit et volo.’ - <cite>Name Surename</cite></p>
  </main>
</body>
</html>
```